Etikett für Rosé Wein
Zielgruppe
Wir sind ein Weingut das Weine im Premiumsegment produziert.
Wir haben vor einen neuen, hochwertigen Roséwein zu launchen. (Ca. 15 Euro Verkaufspreis)
DIe Flaschenform ist dabei an die Premiumweingüter aus der Provence angelehnt. (als Beispiel Silent Meadow als Datei dabei)
Der Wein wird ein Markenwein sein, das bedeutet der Weinname wir in der Vermarktung wichtiger sein als unser Weingutsname. Der Wein wird unter der Bezeichnung LUMARA vermarket werden.
Der Wein wird eine rose- goldende Kapsel erhalten(ähnlich Silent Meadow) - Datei unserer Kapsel anbei.
Folgende Bestandteile müssen am Etikett zu finden sein.
LUMARA
premium organic Rosé
2021(Jahrgang)
Kessel - Logo(nur die Grafik, nicht der Text Weingut Tobias Kessel der unter dem Logo steht)
Eventuell hätten wir noch gerne ein kleines Icon dabei, etwa eine Illustration eines Vogels oder zBsp. eines Blatt als Skelett oder ähnlich. Oder aber/auch das Logo der alpenländischen Erbkellereien könnte als Icon dienen(ebenfalls als Datei dabei)
Aufgabenstellung
Bei diesem Vorderseiten - Flaschenetikett ist uns eine hochwertige, aussagekräftige Etikette wichtig. Das Etikett muss leicht konisch sein, da die Flasche konisch ist. Die Glasfarbe der Flasche ist weiß durchsichtig, sodass die Farbe des Roseweines gut zur Geltung kommt.
Die max. Etikettenhöhe kann 90 mm betragen. Der Winkel der Flasche ist auf der technischen Zeichnun ersichtlich, von unten nach oben verlaufend, sprich im unteren Teil muss das Etikett schmäler sein als im oberen Bereich. Eine technische Zeichnung der Flasche ist als Datei angehängt.
Ebenso 1. Flaschenfoto einer Originalflache des Mitbewerbs(Fiorello), so wird unsere Flaschen ausssehen.

```html
<!DOCTYPE html>
<html lang="de">
<head>
<meta charset="utf-8">
<title>LUMARA – Etikettenvarianten</title>
<link rel="stylesheet" href="https://fonts.googleapis.com/css2?family=Roboto+Condensed:wght@300;400;900&display=swap">
<style>
  :root {
    --stage: #0b0908;
    --label-light: #f6ab72;
    --label-deep: #ec8f52;
    --paper-white: #fbf6f0;
    --plum: #9a3560;
    --signal-red: #e2231a;
    --numeral: #c9c9c9;
  }
  * { margin: 0; padding: 0; box-sizing: border-box; }
  html, body { width: 1200px; height: 1200px; overflow: hidden; background: var(--stage); }
  .lineup { position: relative; width: 1200px; height: 1200px; }
  .label-variant { position: absolute; top: 751px; width: 228px; height: 242px; }
  .label-variant svg { display: block; width: 100%; height: 100%; }
  .variant-1 { left: 70px; }
  .variant-2 { left: 360px; }
  .variant-3 { left: 626px; }
  .variant-4 { left: 907px; }
  .variant-number {
    position: absolute;
    top: 1110px;
    width: 228px;
    text-align: center;
    font-family: "Roboto Condensed", sans-serif;
    font-weight: 400;
    font-size: 34px;
    color: var(--numeral);
  }
  .wordmark { font-family: "Roboto Condensed", sans-serif; font-weight: 900; }
  .descriptor { font-family: "Roboto Condensed", sans-serif; font-weight: 300; }
  .winery-name { font-family: "Roboto Condensed", sans-serif; font-weight: 300; letter-spacing: 0.5px; }
</style>
</head>
<body>
<main class="lineup">
  <svg width="0" height="0" aria-hidden="true" style="position:absolute">
    <defs>
      <linearGradient id="label-fill" x1="0" y1="0" x2="0" y2="1">
        <stop offset="0" stop-color="var(--label-light)"/>
        <stop offset="1" stop-color="var(--label-deep)"/>
      </linearGradient>
    </defs>
  </svg>

  <section class="label-variant variant-1">
    <svg viewBox="0 0 228 242">
      <polygon points="0,0 228,0 224,242 4,242" fill="var(--paper-white)"/>
      <polygon points="6,6 222,6 218,236 10,236" fill="url(#label-fill)"/>
      <text class="winery-name" x="206" y="42" text-anchor="end" font-size="15" fill="var(--plum)">KESSEL</text>
      <circle cx="112" cy="112" r="26" fill="var(--plum)"/>
      <text class="wordmark" x="18" y="184" font-size="26" fill="var(--signal-red)">LUMARA</text>
      <text class="descriptor" x="18" y="210" font-size="20" fill="var(--signal-red)">premium organic Rosé</text>
    </svg>
  </section>
  <div class="variant-number" style="left:70px">1</div>

  <section class="label-variant variant-2">
    <svg viewBox="0 0 228 242">
      <polygon points="0,0 228,0 224,242 4,242" fill="url(#label-fill)"/>
      <text class="wordmark" x="10" y="54" font-size="54" fill="var(--paper-white)" textLength="206" lengthAdjust="spacingAndGlyphs">LUMARA</text>
      <g class="descriptor" fill="var(--paper-white)" font-size="46">
        <text x="12" y="112">premium</text>
        <text x="12" y="164">organic</text>
        <text x="12" y="216">Rosé</text>
      </g>
      <circle cx="186" cy="198" r="30" fill="var(--plum)"/>
      <text class="winery-name" x="186" y="203" text-anchor="middle" font-size="14" fill="var(--paper-white)">KESSEL</text>
    </svg>
  </section>
  <div class="variant-number" style="left:360px">2</div>

  <section class="label-variant variant-3">
    <svg viewBox="0 0 228 242">
      <polygon points="0,0 228,0 224,242 4,242" fill="var(--paper-white)"/>
      <polygon points="6,6 222,6 218,236 10,236" fill="url(#label-fill)"/>
      <text class="wordmark" x="22" y="62" font-size="46" fill="var(--plum)" textLength="186" lengthAdjust="spacingAndGlyphs">LUMARA</text>
      <g class="descriptor" fill="var(--plum)" font-size="40">
        <text x="22" y="112">premium</text>
        <text x="22" y="162">organic</text>
        <text x="22" y="212">Rose</text>
      </g>
      <circle cx="186" cy="146" r="13" fill="var(--signal-red)"/>
      <text class="winery-name" x="204" y="212" text-anchor="end" font-size="13" fill="var(--plum)">KESSEL</text>
    </svg>
  </section>
  <div class="variant-number" style="left:626px">3</div>

  <section class="label-variant variant-4">
    <svg viewBox="0 0 228 242">
      <polygon points="0,0 228,0 224,242 4,242" fill="url(#label-fill)"/>
      <text class="wordmark" x="16" y="62" font-size="48" fill="var(--signal-red)" textLength="196" lengthAdjust="spacingAndGlyphs">LUMARA</text>
      <g class="descriptor" fill="var(--signal-red)" font-size="42">
        <text x="18" y="112">premium</text>
        <text x="18" y="164">organic</text>
        <text x="18" y="216">Rose</text>
      </g>
      <circle cx="188" cy="148" r="14" fill="var(--plum)"/>
      <text class="winery-name" x="208" y="214" text-anchor="end" font-size="13" fill="var(--plum)">KESSEL</text>
    </svg>
  </section>
  <div class="variant-number" style="left:907px">4</div>
</main>
</body>
</html>
```